Plastering (solid plastering) business card design

We need a business card for a a small plastering business based in Perth Western Australia. We are a small team that provides a service in solid plastering specialising in float, white set and sand finish. We would like to see a clean business card with our name "Brightline Plastering" being the focus of the card and maybe incorporated into a logo. We don't have a logo at the moment so we would like to see some cards that may provide us with our future logo.

Industry/Entity Type

Business

Contact Information for Business Card

Brightline Plastering

Solid Plastering Specialists

Ph: Corey 0417683091
Ph: Liam 0468120357

Requirements
Should not have
• The design should not have Drywall incorporated into the card. In perth W.A. Plastering in different to someone that puts up Plyvane. We use sand, cement, lime and hardwall plaster.

```html
<!DOCTYPE html>
<html lang="en">
<head>
<meta charset="utf-8">
<title>Brightline Plastering – Business Card</title>
<link href="https://fonts.googleapis.com/css2?family=Lato:wght@400;700&display=swap" rel="stylesheet">
<style>
  :root {
    --terracotta: #cf7f58;
    --card: #ffffff;
    --backdrop: #ececec;
    --shadow: rgba(0, 0, 0, 0.14);
  }
  * { box-sizing: border-box; margin: 0; padding: 0; }
  html, body {
    width: 1200px;
    height: 846px;
    overflow: hidden;
    background: var(--backdrop);
    font-family: "Lato", "Gill Sans", sans-serif;
  }
  .business-card {
    position: absolute;
    left: 150px;
    top: 158px;
    width: 900px;
    height: 530px;
    background: var(--card);
    border-radius: 28px;
    box-shadow: 0 10px 30px var(--shadow);
    color: var(--terracotta);
  }
  .brand {
    position: absolute;
    left: 0;
    right: 0;
    top: 150px;
    display: flex;
    align-items: center;
    justify-content: center;
    gap: 28px;
  }
  .brand-dot {
    width: 84px;
    height: 84px;
    border-radius: 50%;
    background: var(--terracotta);
    flex: none;
  }
  .brand-name {
    font-weight: 700;
    font-size: 64px;
    line-height: 1;
    letter-spacing: 0.5px;
    color: var(--terracotta);
  }
  .contact-row {
    position: absolute;
    left: 0;
    right: 0;
    bottom: 44px;
    display: flex;
    align-items: stretch;
    justify-content: center;
    font-size: 23px;
    line-height: 1.3;
  }
  .contact-item {
    display: flex;
    align-items: flex-end;
    padding: 4px 30px;
  }
  .contact-item + .contact-item { border-left: 2px solid var(--terracotta); }
  .company-block { flex-direction: column; align-items: center; justify-content: flex-end; }
</style>
</head>
<body>
  <main class="business-card">
    <div class="brand">
      <span class="brand-dot"></span>
      <h1 class="brand-name">Brightline Plastering</h1>
    </div>
    <div class="contact-row">
      <p class="contact-item phone-corey">Corey 04 1768 3091</p>
      <p class="contact-item company-block">
        <span>Brightline Plastering</span>
        <span>Solid Plastering Specialists</span>
      </p>
      <p class="contact-item phone-liam">Liam 04 6812 0357</p>
    </div>
  </main>
</body>
</html>
```